Letterhead for 3 attorney Workers' Comp law firm

We are a 3 attorney law office. We specialize in Workers' Compensation. Our office represents workers who are injured on the job, and the estates of workers who are killed one the job.
When we started our office, we created our own letterhead & have been using it for years. We've just recently hired the 3rd attorney, and were going to just add his name to the letterhead, but have decided we wanted to get a professionally designed letterhead and business cards at this point.
We want something that looks clean and professional. It must look good in black and white because we often make multiple copies of our documents. We're hoping for a design that resonates confidence, reliability and experience.
The design must include the firm name: Dorrance & Pike, PLLC. We would like the PLLC to be small compared to the Dorrance & Pike graphic. We also want to incorporate the attorney names: Ulric Dorrance, Janet Pike, and Lyle Hagberg. Our current letterhead has our contact info in the footer at the bottom of the page. We like that design, but are open to the idea of having it at the top. We'll leave that at the discretion of the designer. Our contact info is as follows: 472 S. Larchmont Avenue, Suite 315 Bellingham, WA 98117 Phone: 360-514-2967, Fax: 360-521-6079, and our website: www.dorrancepike-law.example
Target Market(s)
Clients, courts, other legal offices, doctors offices. These are the people who see our letterhead most frequently. It's not so much for marketing purposes, mainly so that we have a professional image when sending out documents.
Industry/Entity Type
Law Firm
Contact Information for Business Card
On the back of the business card: it can be designed, or be a template for filling in appointment reminder information (i.e. date, time, etc)
Colors
Designer to choose colors to be used in the design.
Requirements
Must have
- Must have our firm name at the top.
- Must include the attorney names.
- Must have all of our contact information (can be at top or bottom - whatever looks best with the design)
Nice to have
- A strong, confident design
Should not have
- We don't want the design to be playful, cartoony or busy.

```html
<!DOCTYPE html>
<html lang="en">
<head>
<meta charset="utf-8">
<title>Dorrance &amp; Pike, PLLC — Letterhead</title>
<link rel="stylesheet" href="https://fonts.googleapis.com/css2?family=Playfair+Display:wght@700&family=Mulish:wght@400&display=swap">
<style>
  :root {
    --backdrop: #d9d9d9;
    --paper: #ffffff;
    --firm-blue: #1d4f7c;
    --names-grey: #5a5a5a;
    --footer-ink: #2e2e2e;
    --page-shadow: rgba(0, 0, 0, 0.28);
  }
  * { margin: 0; padding: 0; box-sizing: border-box; }
  html, body {
    width: 1200px;
    height: 1000px;
    overflow: hidden;
    background: var(--backdrop);
  }
  .letterhead {
    position: absolute;
    left: 315px;
    top: 80px;
    width: 594px;
    height: 841px;
    background: var(--paper);
    box-shadow: 0 4px 10px var(--page-shadow);
    text-align: center;
  }
  .masthead {
    position: absolute;
    top: 34px;
    left: 0;
    right: 0;
  }
  .firm-name {
    font-family: "Playfair Display", Georgia, serif;
    font-weight: 700;
    font-size: 17px;
    color: var(--firm-blue);
    letter-spacing: 0.2px;
    line-height: 1;
  }
  .firm-name .entity {
    font-size: 10px;
    letter-spacing: 0.4px;
  }
  .attorneys {
    margin-top: 10px;
    font-family: "Mulish", Arial, sans-serif;
    font-size: 12px;
    font-variant: small-caps;
    letter-spacing: 1.1px;
    color: var(--names-grey);
    line-height: 1;
  }
  .attorneys .divider {
    display: inline-block;
    width: 1px;
    height: 13px;
    margin: 0 6px;
    background: var(--names-grey);
    vertical-align: -2px;
  }
  .contact-footer {
    position: absolute;
    bottom: 24px;
    left: 0;
    right: 0;
    font-family: "Mulish", Arial, sans-serif;
    font-size: 9px;
    font-variant: small-caps;
    letter-spacing: 1px;
    line-height: 11px;
    color: var(--footer-ink);
  }
  .contact-footer p { margin: 0; }
</style>
</head>
<body>
  <main class="letterhead">
    <header class="masthead">
      <h1 class="firm-name">DORRANCE &amp; PIKE<span class="entity">, PLLC</span></h1>
      <p class="attorneys">
        Ulric Dorrance<span class="divider"></span>Janet Pike<span class="divider"></span>Lyle Hagberg
      </p>
    </header>
    <footer class="contact-footer">
      <p>472 S. Larchmont Avenue, Suite 315 Bellingham, WA 98117</p>
      <p>Phone: 360-514-2967, Fax: 360-521-6079</p>
      <p>www.dorrancepike-law.example</p>
    </footer>
  </main>
</body>
</html>
```